Home page web design for "Tales from Thee"

We need a home page web design for a start up company that will write memoirs for seniors.
The completed project will need to include PSD files...NO HTML or CSS necessary.
Attached is a brief outline concept that may give you some ideas...but you are the creative professionals, so please feel free to add your ideas. We will also attach some files that show you our logo, brochures, and photos that could be used to give you ideas of our focus.
There will need to be access to the other pages on the home page to include: 'About Us'; 'How We Can Help'; 'Community Sessions'; 'Senior Consulting ' and 'Contact Us'.
Updates

Target Market(s)

Seniors and Baby Boomers

Industry/Entity Type

It Company

Number of Pages Required

1 page

Colors
f9ba93
fbca95
faa54b
faf289
f37123

Requirements
Must have
• Script easy on senior eyes.
• Initial contact number would be 844-4LANTERN
Nice to have
• While the color pallet is non-specific we prefer the warm colors.
• salmon, peach.......
• NOT so much the orange of Halloween:)
• However, please utilize your creativity and put in colors you feel will draw best with your design.

```html
<!DOCTYPE html>
<html lang="en">
<head>
<meta charset="utf-8">
<title>Tales from Thee — Home</title>
<link rel="stylesheet" href="https://fonts.googleapis.com/css2?family=Lobster&family=Open+Sans:wght@400;600&display=swap">
<style>
  :root {
    --gold: #b89c5e;
    --gold-dark: #a8894a;
    --heading: #b8954a;
    --phone: #c9a45e;
    --text: #6b6b6b;
    --white: #ffffff;
    --band-top: #d8bf8c;
    --band-bottom: #c6a66a;
    --page: #ffffff;
  }
  * { box-sizing: border-box; margin: 0; padding: 0; }
  html, body { width: 1200px; height: 2651px; overflow: hidden; background: var(--page); }
  body { font-family: "Open Sans", Arial, sans-serif; color: var(--text); position: relative; }
  .script { font-family: "Lobster", cursive; font-weight: 400; }

  .site-header { position: absolute; top: 0; left: 0; width: 1200px; height: 124px; }
  .brand { position: absolute; left: 132px; top: 42px; display: flex; align-items: center; gap: 12px;
           font-family: "Lobster", cursive; font-size: 30px; color: var(--heading); }
  .brand-dot { width: 18px; height: 18px; border-radius: 50%; background: var(--heading); }
  .call { position: absolute; right: 131px; top: 16px; font-size: 21px; color: var(--phone); }
  .social { position: absolute; right: 131px; top: 64px; display: flex; gap: 15px; }
  .social span { width: 31px; height: 31px; border-radius: 50%; display: block; }
  .social span:nth-child(1) { background: #f0c35a; }
  .social span:nth-child(2) { background: #4aa8dc; }
  .social span:nth-child(3) { background: #d9719a; }
  .social span:nth-child(4) { background: #66c6dc; }
  .social span:nth-child(5) { background: #4a6fb4; }

  .main-nav { position: absolute; top: 124px; left: 0; width: 1200px; height: 79px; background: var(--gold); }
  .main-nav a { position: absolute; top: 28px; font-size: 15px; color: var(--white); text-decoration: none; }
  .main-nav a.active { color: #3a3326; }

  .hero { position: absolute; top: 203px; left: 0; width: 1200px; height: 499px;
          background: linear-gradient(100deg, #ece2cf 0%, #d9c6a6 35%, #cfb89a 60%, #eee7da 100%); }
  .hero-arrow { position: absolute; top: 238px; width: 50px; height: 50px; }
  .hero-arrow.prev { left: 12px; } .hero-arrow.next { right: 12px; }
  .hero-caption { position: absolute; left: 714px; top: 272px; width: 353px; height: 159px;
                  background: rgba(184,150,88,0.78); color: var(--white); padding: 22px 26px; font-size: 32px; line-height: 58px; }

  .section-title { font-family: "Lobster", cursive; font-size: 32px; color: var(--heading); text-align: center; font-weight: 400; }
  p { font-size: 14px; line-height: 23px; }

  .welcome { position: absolute; top: 702px; left: 0; width: 1200px; height: 360px; }
  .welcome .section-title { position: absolute; top: 38px; width: 100%; }
  .welcome-photo { position: absolute; left: 132px; top: 106px; width: 258px; height: 199px;
                   background: linear-gradient(135deg, #5a3520, #9a6a45 55%, #c7b8b0); }
  .welcome-text { position: absolute; left: 430px; top: 98px; width: 639px; }
  .welcome-text p + p { margin-top: 14px; }

  .help-band { position: absolute; top: 1062px; left: 0; width: 1200px; height: 419px;
               background: linear-gradient(180deg, var(--band-top), var(--band-bottom)); text-align: center; }
  .help-band .section-title { color: var(--white); margin-top: 38px; }
  .help-band .copy { width: 884px; margin: 18px auto 0; color: var(--white); }
  .help-band .copy p + p { margin-top: 23px; }
  .btn-outline { position: absolute; left: 495px; top: 307px; width: 210px; height: 59px; border: 2px solid var(--white);
                 color: var(--white); font-size: 18px; line-height: 55px; text-align: center; }

  .genealogy { position: absolute; top: 1481px; left: 0; width: 1200px; height: 504px; }
  .genealogy .section-title { position: absolute; top: 46px; width: 100%; }
  .genealogy .intro { position: absolute; top: 112px; left: 140px; width: 920px; text-align: center; }
  .occasion { position: absolute; top: 198px; width: 279px; text-align: center; }
  .occasion .frame { height: 201px; background: var(--white); border: 1px solid #ddd; padding: 9px;
                     box-shadow: 0 14px 12px -10px rgba(0,0,0,0.35); }
  .occasion .photo { height: 181px; }
  .occasion .label { margin-top: 25px; font-family: "Lobster", cursive; font-size: 27px; color: var(--heading); }

  .gift-band { position: absolute; top: 1985px; left: 0; width: 1200px; height: 298px;
               background: linear-gradient(90deg, #c9aa70, #b89558 60%, #c2a36b); }
  .gift-lines { position: absolute; left: 129px; top: 36px; color: var(--white); font-size: 32px; }
  .gift-lines div { position: absolute; white-space: nowrap; }
  .gift-photo { position: absolute; left: 777px; top: 47px; width: 290px; height: 201px; border: 2px solid var(--white);
                background: linear-gradient(150deg, #f2e2c0, #e2c99a 60%, #c7a877); }

  .community { position: absolute; top: 2283px; left: 0; width: 1200px; height: 290px; text-align: center; }
  .community .section-title { margin-top: 42px; }
  .community .copy { width: 940px; margin: 16px auto 0; }
  .btn-solid { position: absolute; left: 488px; top: 168px; width: 222px; height: 58px; background: var(--gold);
               color: var(--white); font-size: 18px; line-height: 58px; }

  .site-footer { position: absolute; top: 2573px; left: 0; width: 1200px; height: 78px; background: var(--gold); }
  .site-footer p { position: absolute; left: 129px; top: 28px; font-size: 14px; color: var(--white); }
</style>
</head>
<body>
  <header class="site-header">
    <div class="brand"><span class="brand-dot"></span>Tales from Thee</div>
    <div class="call">Call Us : 800-555-0142</div>
    <div class="social" aria-label="Social links"><span></span><span></span><span></span><span></span><span></span></div>
  </header>

  <nav class="main-nav">
    <a class="active" href="#" style="left:132px">Home</a>
    <a href="#" style="left:235px">About us</a>
    <a href="#" style="left:357px">How we can help</a>
    <a href="#" style="left:537px">Community services</a>
    <a href="#" style="left:744px">Senior consulting services</a>
    <a href="#" style="left:991px">Contact us</a>
  </nav>

  <section class="hero" role="img" aria-label="Smiling senior couple looking at a laptop at home">
    <svg class="hero-arrow prev" viewBox="0 0 50 50"><circle cx="25" cy="25" r="23" fill="rgba(120,110,100,0.25)" stroke="#8a8070" stroke-width="2"/><path d="M29 15 L19 25 L29 35" fill="none" stroke="#6f665a" stroke-width="3"/></svg>
    <svg class="hero-arrow next" viewBox="0 0 50 50"><circle cx="25" cy="25" r="23" fill="rgba(120,110,100,0.25)" stroke="#8a8070" stroke-width="2"/><path d="M21 15 L31 25 L21 35" fill="none" stroke="#6f665a" stroke-width="3"/></svg>
    <div class="hero-caption script">Ordinary lives.........<br>Extraordinary legacies</div>
  </section>

  <section class="welcome">
    <h2 class="section-title">Welcome to Tales from Thee</h2>
    <div class="welcome-photo" role="img" aria-label="Senior woman writing at a lamplit desk"></div>
    <div class="welcome-text">
      <p>Lorem ipsum dolor sit amet, duo ne dictas vivendo. Libris noluisse intellegebat pri ne, causae pertinax mel ea. Ad qui agam facilis gloriatur, quis efficiantur quo ne. Tempor meliore qualisque ut cum. Maiestatis consequuntur mea et, cu pro mentitum maluisset interpretaris. Ad semper quaeque consulatu eam, sea viris propriae ne.</p>
      <p>Maiestatis consequuntur mea et, cu pro mentitum maluisset interpretaris. Ad semper quaeque consulatu eam, sea viris propriae ne.Maiestatis consequuntur mea et, cu pro mentitum maluisset interpretaris. Ad semper quaeque consulatu eam, sea viris propriae ne.Maiestatis consequuntur mea et, cu pro mentitum maluisset interpretaris.</p>
    </div>
  </section>

  <section class="help-band">
    <h2 class="section-title">How We Can Help</h2>
    <div class="copy">
      <p>Sea id ullum scripta maiorum, ea meis munere vim. Dicat instructior cum cu, an pri diceret torquatos. Quo et iudicabit temporibus, explicari voluptaria ei eos. Sumo homero quo ex, alia sonet qui ne. Ad natum dicam per, periculis honestatis ex eam.Quo et iudicabit temporibus, explicari voluptaria ei eos. Sumo homero quo ex, alia sonet qui ne.</p>
      <p>Sea id ullum scripta maiorum, ea meis munere vim. Dicat instructior cum cu, an pri diceret torquatos. Quo et iudicabit temporibus, explicari voluptaria ei eos. Sumo homero quo ex, alia sonet qui ne. Ad natum dicam per, periculis honestatis ex eam.Quo et iudicabit temporibus, explicari voluptaria ei eos. Sumo homero quo ex, alia sonet qui ne.</p>
    </div>
    <div class="btn-outline">View more details</div>
  </section>

  <section class="genealogy">
    <h2 class="section-title">When a Genealogy Doesn't Say Enough</h2>
    <p class="intro">Lorem ipsum dolor sit amet, duo ne dictas vivendo. Libris noluisse intellegebat pri ne, causae pertinax mel ea. Ad qui agam facilis gloriatur, quis efficiantur quo ne. Tempor meliore qualisque ut cum. Maiestatis consequuntur mea et.</p>
    <div class="occasion" style="left:131px">
      <div class="frame"><div class="photo" role="img" aria-label="Grandmother and child with a birthday cake" style="background:linear-gradient(135deg,#2e3f78,#7a5a6a 55%,#d8b48a)"></div></div>
      <div class="label">Birthday</div>
    </div>
    <div class="occasion" style="left:460px">
      <div class="frame"><div class="photo" role="img" aria-label="Family celebrating an anniversary" style="background:linear-gradient(135deg,#d8d4cc,#7f95b8 55%,#e9e4dc)"></div></div>
      <div class="label">Anniversary</div>
    </div>
    <div class="occasion" style="left:789px">
      <div class="frame"><div class="photo" role="img" aria-label="Family gathered at Christmas" style="background:linear-gradient(135deg,#6a2a22,#a84a3a 50%,#3a2a24)"></div></div>
      <div class="label">Christmas</div>
    </div>
  </section>

  <section class="gift-band">
    <div class="gift-lines script">
      <div style="top:0">Sometimes a commitment is all we need to</div>
      <div style="top:44px">get started.</div>
      <div style="top:108px">let us help chronicle your journey.</div>
      <div style="top:176px">Tales from Thee makes a great gift idea!</div>
    </div>
    <div class="gift-photo" role="img" aria-label="Fountain pen resting on a handwritten letter"></div>
  </section>

  <section class="community">
    <h2 class="section-title">Community Sessions</h2>
    <p class="copy">Sea id ullum scripta maiorum, ea meis munere vim. Dicat instructior cum cu, an pri diceret torquatos. Quo et iudicabit temporibus, explicari voluptaria ei eos. Sumo homero quo ex, alia sonet qui ne. Ad natum dicam per, periculis honestatis ex eam.</p>
    <div class="btn-solid">View more details</div>
  </section>

  <footer class="site-footer">
    <p>Copyright @ 2014 Talesfromthee.All Rights Reserved.</p>
  </footer>
</body>
</html>
```